Innovative Consulting Firm Needs New Business Cards and Stationary

Our Innovative Consulting Firm, Larkfield Consulting, is in need of new business cards and stationary designs. We want two-sided cards that incorporate our logo, which is attached. We are looking for something not too formal, but is professional and slick.

Card should have the following information:
Name (ex. Tom Bradley)
Title (ex. Manager)
Address (ex. 24680 Cedar Lane)
Address 2 (ex. Suite 100)
City
State
Zip Code
Mobile
Email

The card should also have our website: www.larkfieldconsulting.example

Industry/Entity Type

Management Consulting

Contact Information for Business Card

Name (ex. Tom Bradley)
Title (ex. Manager)
Address 2 (ex. Suite 100)
City
State
Zip Code
Mobile
Email

Font styles to use
Sans Serif

Requirements
Must have
• The colors on the card must match the colors in the logo. The exact color codes are attached in a pdf.
Nice to have
• The Company's Tagline is "Focused on your Future". This might be nice to incorporate, but not necessary.

```html
<!DOCTYPE html>
<html lang="en">
<head>
<meta charset="utf-8">
<title>Larkfield Consulting – Business Cards</title>
<link rel="stylesheet" href="https://fonts.googleapis.com/css2?family=Didact+Gothic&family=Open+Sans:wght@400;700&display=swap">
<style>
  :root {
    --brand-blue: #1d4f7c;
    --brand-gold: #f5b21a;
    --card-white: #ffffff;
    --ink: #1a1a1a;
    --backdrop: #2e241d;
  }
  * { margin: 0; padding: 0; box-sizing: border-box; }
  html, body {
    width: 1200px;
    height: 1160px;
    overflow: hidden;
    background: var(--backdrop);
  }
  .canvas {
    position: relative;
    width: 1200px;
    height: 1160px;
  }
  .card {
    position: absolute;
    left: 278px;
    width: 668px;
    height: 380px;
    border-radius: 16px;
    overflow: hidden;
    box-shadow: 0 6px 14px rgba(0, 0, 0, 0.45);
  }
  .card--front { top: 146px; background: var(--card-white); }
  .card--back  { top: 574px; background: var(--brand-blue); }

  .chevron-panel {
    position: absolute;
    left: 0; top: 0;
    width: 260px; height: 380px;
  }
  .holder {
    position: absolute;
    left: 24px;
    top: 172px;
    max-width: 176px;
    color: var(--card-white);
    font-family: "Didact Gothic", sans-serif;
  }
  .holder__name {
    font-size: 24px;
    letter-spacing: 0;
    word-spacing: -2px;
    line-height: 1;
    white-space: nowrap;
  }
  .holder__title {
    font-size: 17px;
    letter-spacing: 0.8px;
    margin-top: 9px;
  }

  .brand {
    font-family: "Open Sans", sans-serif;
    font-weight: 700;
    display: flex;
    align-items: center;
    gap: 10px;
  }
  .brand__dot {
    width: 14px; height: 14px;
    border-radius: 50%;
    background: var(--brand-gold);
  }
  .brand--front {
    position: absolute;
    right: 37px;
    top: 80px;
    font-size: 31px;
    color: var(--brand-blue);
  }
  .brand--back {
    position: absolute;
    left: 0; right: 0;
    top: 148px;
    justify-content: center;
    font-size: 40px;
    color: var(--card-white);
  }

  .contact {
    position: absolute;
    right: 37px;
    top: 176px;
    text-align: right;
    font-family: "Open Sans", sans-serif;
    font-size: 18px;
    color: var(--ink);
    line-height: 27px;
  }
  .contact__web {
    font-weight: 700;
    letter-spacing: 0.4px;
    margin-top: 5px;
  }
  .contact__address { margin-top: 35px; }
</style>
</head>
<body>
<div class="canvas">
  <section class="card card--front">
    <svg class="chevron-panel" viewBox="0 0 260 380" aria-hidden="true">
      <polygon points="0,0 122,0 218,190 122,380 0,380" fill="var(--brand-blue)"/>
      <polygon points="122,0 154,0 248,190 154,380 122,380 218,190" fill="var(--brand-gold)"/>
    </svg>
    <div class="holder">
      <p class="holder__name">TOM BRADLEY</p>
      <p class="holder__title">Manager</p>
    </div>
    <div class="brand brand--front">
      <span class="brand__dot"></span>
      <span>Larkfield Consulting</span>
    </div>
    <div class="contact">
      <p>012.345.6789</p>
      <p>info@larkfieldconsulting.example</p>
      <p class="contact__web">www.larkfieldconsulting.example</p>
      <p class="contact__address">24680 Cedar Lane, Suite 100<br>Cityname, State 00000</p>
    </div>
  </section>

  <section class="card card--back">
    <div class="brand brand--back">
      <span class="brand__dot"></span>
      <span>Larkfield Consulting</span>
    </div>
  </section>
</div>
</body>
</html>
```